Valve bag design

I need a valve bag for 25kg wall putty bag

Here are attached bags for reference

Most of the words or design you can copy from talvuno bag attached and company profile
Also I have attached our local product for reference

```html
<!DOCTYPE html>
<html lang="en">
<head>
<meta charset="utf-8">
<title>Kestrel Coat Wall Putty – 25kg Valve Bag</title>
<link href="https://fonts.googleapis.com/css2?family=Anton&family=Poppins:wght@400;500;600;700&display=swap" rel="stylesheet">
<style>
:root{
  --navy:#2a3f72;
  --navy-deep:#233766;
  --taupe:#b1a6a0;
  --taupe-light:#d9d4d1;
  --white:#ffffff;
  --ink:#1f2533;
  --cell:#cfe0ef;
  --canvas:#eceef1;
}
*{margin:0;padding:0;box-sizing:border-box}
html,body{width:800px;height:1200px;overflow:hidden}
body{background:var(--canvas);font-family:'Poppins',sans-serif;color:var(--ink);position:relative}
.panel{position:absolute;top:317px;width:376px;height:565px;background:var(--white);overflow:hidden;box-shadow:0 4px 14px rgba(0,0,0,.12)}
.panel--front{left:16px}
.panel--back{left:408px}
.panel-shapes{position:absolute;inset:0;width:100%;height:100%}
.abs{position:absolute}

/* front */
.side-title{left:65px;top:247px;transform:translate(-50%,-50%) rotate(-90deg);font-family:'Anton',sans-serif;font-size:92px;letter-spacing:2px;color:var(--white);white-space:nowrap;line-height:1}
.brand-name{font-family:'Poppins',sans-serif;font-weight:700;color:var(--navy);white-space:nowrap;letter-spacing:.5px}
.brand-mark{display:inline-block;background:var(--navy);vertical-align:middle}
.front-brand{left:152px;top:52px;width:190px;text-align:center}
.front-brand .brand-mark{width:22px;height:22px;margin-bottom:6px}
.front-brand .brand-name{font-size:14.5px;display:block}
.product-heading{left:150px;top:104px;line-height:.98}
.product-heading .h-white,.product-heading .h-cement{font-weight:700;color:var(--navy);font-size:24.5px;display:block}
.product-heading .h-putty{font-weight:700;color:var(--taupe);font-size:40px;display:block;line-height:1}
.heading-rule{left:151px;top:188px;width:100px;height:1.5px;background:var(--navy)}
.tagline{left:150px;top:209px;width:210px;font-size:9px;font-weight:500;line-height:1.25}
.features{left:146px;width:220px;display:flex}
.features--top{top:258px}
.features--bottom{top:321px;left:156px;width:180px}
.feature{flex:1;text-align:center;font-size:6.3px;font-weight:500;line-height:1.2;padding:0 2px;border-left:.6px solid #ccd2de}
.feature:first-child{border-left:none}
.feature-icon{display:block;margin:0 auto 3px;width:20px;height:20px}
.pack-weight{font-family:'Poppins',sans-serif;font-weight:700;color:var(--navy);line-height:1;white-space:nowrap}
.pack-weight small{font-size:.5em;color:var(--white);margin-left:2px}
.front-weight{left:258px;top:486px;font-size:40px;letter-spacing:-2px}
.front-weight small{letter-spacing:0}

/* back */
.back-title{left:24px;top:18px;font-family:'Anton',sans-serif;font-size:64px;color:var(--navy);letter-spacing:3px;line-height:1;white-space:nowrap}
.back-subtitle{left:27px;top:125px;font-size:11.5px;font-weight:600;color:var(--navy)}
.back-brand{left:206px;top:118px;width:124px;text-align:center}
.back-brand .brand-mark{width:22px;height:22px;margin-bottom:5px}
.back-brand .brand-name{font-size:12.5px;display:block}
.description{left:27px;top:145px;width:152px;font-size:6px;line-height:1.23}
.description b{font-weight:600}
.hl{color:var(--navy);font-weight:500}
.instructions{left:27px;top:224px;width:325px;font-size:5.9px;line-height:1.25}
.instructions p{margin-bottom:5px}
.instructions .sub{color:var(--navy);font-weight:500;display:block}
.spec{left:26px;top:431px;width:190px}
.spec-head{background:var(--navy);color:var(--white);font-size:7.5px;font-weight:500;padding:2px 6px;border-radius:2px;letter-spacing:.3px}
.spec-row{display:flex;gap:2px;margin-top:2px}
.spec-row span{background:var(--cell);font-size:5.8px;padding:3px 6px;border-radius:1px}
.spec-row span:first-child{width:94px}
.spec-row span:last-child{flex:1}
.back-weight{left:250px;top:448px;font-size:40px;letter-spacing:-2px}
.back-weight small{letter-spacing:0}
.footer{left:0;top:506px;width:376px;height:59px;background:var(--navy);color:var(--white);padding:6px 24px}
.footer-lead{font-size:9.5px;font-weight:500;color:var(--taupe-light);line-height:1.1}
.footer-company{font-size:7.5px;color:var(--taupe-light);line-height:1.2}
.footer-contacts{display:flex;justify-content:space-between;margin-top:6px;font-size:5.8px}
.footer-contacts span{display:flex;align-items:center;gap:2px}
.footer-contacts svg{width:6px;height:6px}
</style>
</head>
<body>

<section class="panel panel--front" aria-label="Bag front">
  <svg class="panel-shapes" viewBox="0 0 665 1000" preserveAspectRatio="none" aria-hidden="true">
    <rect x="0" y="0" width="225" height="1000" fill="var(--navy)"/>
    <polygon points="565,0 665,0 665,25 625,100 525,100 585,0" fill="var(--taupe-light)" opacity=".6"/>
    <polygon points="620,25 665,25 665,100 600,100" fill="var(--taupe-light)" opacity=".4"/>
    <polygon points="345,703 665,703 665,1000 0,1000 0,875 225,875 225,810 285,810" fill="var(--navy)"/>
    <polygon points="225,810 285,810 205,935 165,935 165,1000 0,1000 0,935 160,935" fill="var(--white)"/>
    <polygon points="120,935 200,935 150,1000 70,1000" fill="var(--taupe)" opacity=".7"/>
    <polygon points="330,740 395,740 330,860 265,860" fill="var(--taupe)" opacity=".7"/>
    <polygon points="590,710 640,710 590,800 540,800" fill="var(--taupe)" opacity=".45"/>
    <polygon points="455,838 665,838 665,1000 385,1000" fill="var(--taupe)"/>
  </svg>

  <div class="abs side-title">WALL PUTTY</div>

  <div class="abs front-brand"><span class="brand-mark"></span><span class="brand-name">KESTREL COAT</span></div>

  <h1 class="abs product-heading">
    <span class="h-white">WHITE</span>
    <span class="h-cement">CEMENT BASED</span>
    <span class="h-putty">PUTTY</span>
  </h1>
  <div class="abs heading-rule"></div>
  <p class="abs tagline">Premium wall putty to use for cement based plaster o concrete surfaces before part</p>

  <div class="abs features features--top">
    <div class="feature"><svg class="feature-icon" viewBox="0 0 20 20"><circle cx="10" cy="10" r="9.5" fill="var(--navy)"/><circle cx="10" cy="10" r="7.5" fill="none" stroke="#fff" stroke-width=".6"/><path d="M10 5.5l1 3 3 1-3 1-1 3-1-3-3-1 3-1z" fill="#fff"/></svg>Very smooth &amp; glossy finish</div>
    <div class="feature"><svg class="feature-icon" viewBox="0 0 20 20"><circle cx="10" cy="10" r="9.5" fill="var(--navy)"/><circle cx="10" cy="10" r="7.5" fill="none" stroke="#fff" stroke-width=".6"/><path d="M5.5 13l4.5-6 4.5 6z" fill="none" stroke="#fff" stroke-width=".9"/></svg>Suitable for all cement surfaces</div>
    <div class="feature"><svg class="feature-icon" viewBox="0 0 20 20"><circle cx="10" cy="10" r="9.5" fill="var(--navy)"/><circle cx="10" cy="10" r="7.5" fill="none" stroke="#fff" stroke-width=".6"/><rect x="6" y="7" width="8" height="6" fill="none" stroke="#fff" stroke-width=".9"/><path d="M6 10h8M10 7v6" stroke="#fff" stroke-width=".6"/></svg>Suitable for Interior of exterior</div>
    <div class="feature"><svg class="feature-icon" viewBox="0 0 20 20"><circle cx="10" cy="10" r="9.5" fill="var(--navy)"/><circle cx="10" cy="10" r="7.5" fill="none" stroke="#fff" stroke-width=".6"/><path d="M6 13l6-6 2 2-6 6H6z" fill="none" stroke="#fff" stroke-width=".9"/></svg>Very high tensile adhesion</div>
  </div>
  <div class="abs features features--bottom">
    <div class="feature"><svg class="feature-icon" viewBox="0 0 20 20"><circle cx="10" cy="10" r="9.5" fill="var(--navy)"/><circle cx="10" cy="10" r="7.5" fill="none" stroke="#fff" stroke-width=".6"/><path d="M10 5.5c2 3 3 4.5 3 6a3 3 0 01-6 0c0-1.5 1-3 3-6z" fill="none" stroke="#fff" stroke-width=".9"/></svg>Very low water absorption</div>
    <div class="feature"><svg class="feature-icon" viewBox="0 0 20 20"><circle cx="10" cy="10" r="9.5" fill="var(--navy)"/><circle cx="10" cy="10" r="7.5" fill="none" stroke="#fff" stroke-width=".6"/><circle cx="10" cy="10" r="3.5" fill="none" stroke="#fff" stroke-width=".9"/></svg>No water caring, needed</div>
    <div class="feature"><svg class="feature-icon" viewBox="0 0 20 20"><circle cx="10" cy="10" r="9.5" fill="var(--navy)"/><circle cx="10" cy="10" r="7.5" fill="none" stroke="#fff" stroke-width=".6"/><path d="M7 10l2 2 4-4" fill="none" stroke="#fff" stroke-width="1"/></svg>Very high coverage &amp; easy to apply</div>
  </div>

  <div class="abs pack-weight front-weight">25<small>KG</small></div>
</section>

<section class="panel panel--back" aria-label="Bag back">
  <svg class="panel-shapes" viewBox="0 0 665 1000" preserveAspectRatio="none" aria-hidden="true">
    <polygon points="420,758 665,758 665,900 365,900" fill="var(--taupe)"/>
  </svg>

  <div class="abs back-title">WALL PUTTY</div>
  <h2 class="abs back-subtitle">Kestrel Coat Wall Putty</h2>
  <div class="abs back-brand"><span class="brand-mark"></span><span class="brand-name">KESTREL COAT</span></div>

  <p class="abs description"><b>Descriptions</b> <span class="hl">kestrel coat</span> is a white Cement based wall puty which provides an ideal proshing for concrete I cement plastered walls and cellings. It reduces paint consumption, provides an concrete / eor painting and moisture resistant educes painst for further mealication or at dinasor paints. (it is very important to understand that morsture resistance means resistance kinds ter in humid air and not physical wales tantaca maisases)</p>

  <div class="abs instructions">
    <p><span class="sub">Application recommendations</span>Apply on cement concrete /cement plaster surfaces, wallboard and sypsum/plaster</p>
    <p>25 kg of <span class="hl">Kestrel Coat Wall Putty</span> is added to approximatieectriC liter, of clean Water, mixing may be Wont mart is added using drsurtable electric mifor</p>
    <p>Prepared mortar is left to mature toy or by minutes and mixed again before use.<br>The mortar must be used in 2 - 3 hours.</p>
    <p>Remove all dust, loose particles from the surface, oil, paint, curing agent, lime and silicones before application of Kestrel Coat Wall Putty</p>
    <p><span class="sub">Kestrel Coat Wall Putty Plus</span>Ensure that the surface is moisturized before the application, cracks and holes must be repaired with appropriate mortar.</p>
    <p>Apply 19 coat of <span class="hl">Kestrel Coat Wall Putty</span> (1.5 mm thickness) using a blade / spatula on the wall with a "bottom to up" configuration</p>
    <p>Apply 2nd coat of <span class="hl">Kestrel Coat Wall Putty</span> (1.0 mm thickness) preferably after 4 hours during summers, and after 12 hours during winters. Second coat shall be applied <b class="hl">"horizontally"</b> to even out application marks of 1st coat, if any.</p>
    <p>Consumption: Approximately 1kg/m (for 1 mm thickness)<br><span class="hl">Shelf life:</span> Unopened bag can be stored in dry environment for up to 12 months, staked</p>
  </div>

  <div class="abs spec">
    <div class="spec-head">PRODUCT SPECIFICATION</div>
    <div class="spec-row"><span>Comprensive Strength</span><span>28 days- 14 N/mm</span></div>
    <div class="spec-row"><span>Adhesion Strength</span><span>28 days- 2.38 N/mm</span></div>
    <div class="spec-row"><span>Water requirement volume</span><span>38%</span></div>
  </div>

  <div class="abs pack-weight back-weight">25<small>KG</small></div>

  <footer class="abs footer">
    <div class="footer-lead">Marketed and distributed by</div>
    <div class="footer-company">Morlan Build Ltd</div>
    <div class="footer-contacts">
      <span><svg viewBox="0 0 10 10"><circle cx="5" cy="5" r="5" fill="#fff"/><path d="M3 2.5l1 1-.6.8a4 4 0 002.3 2.3l.8-.6 1 1-.8.8C4.5 7.5 2.5 5.5 2.2 3.3z" fill="var(--navy)"/></svg>+255700000000</span>
      <span><svg viewBox="0 0 10 10"><circle cx="5" cy="5" r="4.2" fill="none" stroke="#fff" stroke-width="1"/></svg>info@morlanbuild.com</span>
      <span><svg viewBox="0 0 10 10"><circle cx="5" cy="5" r="4.2" fill="none" stroke="#fff" stroke-width="1"/><path d="M1 5h8M5 1c2 2.5 2 5.5 0 8M5 1c-2 2.5-2 5.5 0 8" fill="none" stroke="#fff" stroke-width=".6"/></svg>www.morlanbuild.com</span>
    </div>
  </footer>
</section>

</body>
</html>
```